Stand out flyer needed for Boxing gym

Hi we need a trifold brochure designed for our outdoor boxing business it will be delivered to doctors and nutritionists to help their patients be healthier and get fit.We have supplied high res pictures for you to use in the brochure. We need a design that use a lot of yellow so it captures their attention. You can check our website for design colours www.ridgepunch.com.au

Target Market(s)

Overweight or unfit people looking to change their lives

Industry/Entity Type

Health And Wellness

Font styles to use
Sans Serif

Colors
fbee3d
ffffff
000000

Requirements
Must have
• (main heading - large bold font) Get fit lose weight & feel great
• (bold) Unlimited outdoor boxing classes $14.95
• Complete affordability & No judgements guaranteed
• (bold) Tailored programs (bold)
• Our programs are structured so that members of all fitness levels feel confident & comfortable during their start-up phase allowing you to quickly build your fitness
• (bold) Injury prevention (bold)
• Our training systems include techniques that will help you avoid injuries and build balanced strength
• (bold) Strengthen & Tone your core (bold)
• You're core muscles are some of you're most important muscles. Each workout you do incorporates core exercises to help avoid injuries and make you're total body stronger
• (bold) Wake up with more energy(bold)
• Every class you'll do will have you filled with energy the will pump you up for the rest of your day
• (bold) Sleep better(bold)
• One of the best parts of exercise is the benefit it has on your sleeping patterns. You'll sleep deeper & more sound
• (bold) Supportive environment (bold)
• At RIDGE PUNCH you'll be surrounded by trainers & other members who are there to encourage & motivate you to reach your goals and to get you moving more.
• Coupon code: SunRise27

```html
<!DOCTYPE html>
<html lang="en">
<head>
<meta charset="utf-8">
<title>Ridge Punch – Trifold Brochure</title>
<link rel="stylesheet" href="https://fonts.googleapis.com/css2?family=Bebas+Neue&family=Open+Sans:wght@400;700;800&display=swap">
<style>
  :root{
    --yellow:#fbee3d;
    --black:#000000;
    --ink:#141414;
    --panel:#1b1b1b;
    --white:#ffffff;
    --paper:#f1f1f1;
    --grey:#3a3a3a;
    --muted:#bdbdbd;
    --bg:#e4e4e4;
  }
  *{box-sizing:border-box;margin:0;padding:0}
  html,body{width:1200px;height:2400px;overflow:hidden;background:var(--bg)}
  body{font-family:'Open Sans',Arial,sans-serif;position:relative}
  .sheet{position:absolute;left:60px;width:1080px;height:764px;display:flex;box-shadow:0 18px 40px rgba(0,0,0,.25)}
  .sheet--outside{top:200px}
  .sheet--inside{top:1436px}
  .panel{position:relative;width:360px;height:764px;overflow:hidden;background:var(--panel);color:var(--white)}
  .panel + .panel{border-left:1px solid rgba(255,255,255,.06)}
  .layer{position:absolute;left:0;top:0;width:100%;height:100%}
  .head{font-family:'Bebas Neue',Impact,sans-serif;font-weight:400;letter-spacing:.5px;line-height:1}
  .brand{display:inline-flex;align-items:center;gap:10px;font-family:'Bebas Neue',Impact,sans-serif;font-size:40px;letter-spacing:2px;color:var(--white);line-height:1;white-space:nowrap}
  .brand__mark{width:14px;height:14px;background:var(--yellow)}
  .brand--yellow{color:var(--yellow)}

  /* outside: offer flap */
  .offer{position:absolute;left:34px;top:60px;width:290px}
  .offer__price{font-size:64px;color:var(--yellow)}
  .offer__title{font-size:34px;color:var(--white);margin-top:6px}
  .offer__note{font-size:13px;color:var(--muted);margin-top:14px;line-height:1.4;width:180px}
  .coupon{position:absolute;left:20px;top:292px;width:250px;height:46px;border-radius:23px;background:var(--yellow);color:var(--black);font-family:'Bebas Neue',Impact,sans-serif;font-size:22px;display:flex;align-items:center;justify-content:center;letter-spacing:.5px;white-space:nowrap}

  /* outside: contact */
  .contact{position:absolute;left:0;top:50px;width:360px;text-align:center}
  .contact__title{font-size:32px;margin-top:26px;color:var(--white)}
  .map{position:absolute;left:105px;top:220px;width:150px;height:150px;border-radius:50%;background:radial-gradient(circle at 40% 40%,#f4f4f4,#c9c9c9);border:4px solid var(--white)}
  .locations{position:absolute;left:44px;top:400px;width:280px;list-style:none}
  .locations li{margin-bottom:10px;font-size:11.5px;line-height:1.35;color:var(--muted)}
  .locations strong{display:block;font-family:'Bebas Neue',Impact,sans-serif;font-weight:400;font-size:19px;color:var(--yellow);letter-spacing:.5px}
  .contact__phone,.contact__mail{position:absolute;left:44px;font-family:'Bebas Neue',Impact,sans-serif;color:var(--yellow);white-space:nowrap}
  .contact__phone{top:650px;font-size:30px}
  .contact__mail{top:688px;font-size:24px}

  /* outside: cover */
  .cover__brand{position:absolute;left:80px;top:50px}
  .cover__title{position:absolute;left:10px;top:128px;width:340px;font-size:40px;color:var(--yellow);text-align:center;white-space:nowrap;line-height:1.05}
  .cover__url{position:absolute;left:0;top:692px;width:360px;text-align:center;font-weight:800;font-size:22px;color:var(--black);white-space:nowrap}

  /* inside */
  .panel--light{background:linear-gradient(180deg,#ffffff 0%,#ececec 100%);color:var(--ink)}
  .tag{position:absolute;left:0;top:56px;background:var(--ink);color:var(--white);font-size:17px;font-weight:800;padding:8px 26px 8px 24px;border-right:6px solid var(--yellow);text-transform:uppercase;white-space:nowrap}
  .benefit{position:absolute;width:290px}
  .benefit__title{font-weight:800;font-size:17px;text-transform:uppercase;margin-bottom:8px}
  .benefit__text{font-size:13.5px;line-height:1.45}
  .panel--light .benefit{left:34px}
  .panel--light .benefit__text{color:#333}
  .benefit--yellow .benefit__title{color:var(--yellow)}
  .panel:not(.panel--light) .benefit__text{color:#d6d6d6}
  .promise{position:absolute;left:0;top:624px;width:660px;height:48px;background:var(--grey);color:var(--white);font-weight:800;font-size:21px;display:flex;align-items:center;padding-left:34px;letter-spacing:.3px;white-space:nowrap;z-index:5}
  .inside-url{position:absolute;left:34px;top:700px;font-weight:800;font-size:22px;color:var(--ink);white-space:nowrap}
</style>
</head>
<body>

<!-- Outside of the trifold -->
<section class="sheet sheet--outside" aria-label="Brochure outside">

  <article class="panel panel--offer">
    <svg class="layer" viewBox="0 0 360 764" role="img" aria-label="Photo of people boxing outdoors in a sunlit park">
      <defs>
        <linearGradient id="park" x1="0" y1="0" x2="1" y2="1">
          <stop offset="0" stop-color="#e8d48a"/>
          <stop offset=".5" stop-color="#7d8e4a"/>
          <stop offset="1" stop-color="#36461f"/>
        </linearGradient>
      </defs>
      <path d="M0 430 C 110 400, 230 420, 360 470 L360 764 L0 764 Z" fill="url(#park)"/>
    </svg>
    <svg class="layer" viewBox="0 0 360 764" aria-hidden="true">
      <path d="M0 412 C 110 380, 240 400, 360 452 L360 474 C 240 424, 110 402, 0 432 Z" fill="var(--yellow)"/>
      <path d="M250 764 C 300 700, 340 640, 360 600 L360 764 Z" fill="var(--panel)"/>
      <path d="M236 764 C 290 696, 330 634, 360 586 L360 604 C 336 648, 298 706, 254 764 Z" fill="var(--yellow)"/>
    </svg>
    <div class="offer">
      <p class="offer__price head">$14.95</p>
      <p class="offer__title head">Unlimited outdoor<br>boxing classes</p>
      <p class="offer__note">Complete affordability &amp; No judgements guaranteed!</p>
    </div>
    <p class="coupon">Coupon code: SunRise27</p>
  </article>

  <article class="panel panel--contact">
    <div class="contact">
      <span class="brand brand--yellow"><span class="brand__mark"></span>RIDGE PUNCH</span>
      <p class="contact__title head">Contact us today<br>for more information</p>
    </div>
    <div class="map" role="img" aria-label="Street map marking the four training locations"></div>
    <ul class="locations">
      <li><strong>Hollowbrook</strong>14 Larch Rd, Hollowbrook NSW 2290</li>
      <li><strong>Westmere</strong>8 Quarry Ln, Westmere NSW 2291</li>
      <li><strong>Elmvale</strong>52 Fenwick St, Elmvale NSW 2292</li>
      <li><strong>Corran</strong>30 Tidewell Rd, Corran NSW 2293</li>
    </ul>
    <p class="contact__phone">0412 555 018</p>
    <p class="contact__mail">info@ridgepunch.com.au</p>
  </article>

  <article class="panel panel--cover">
    <svg class="layer" viewBox="0 0 360 764" role="img" aria-label="Black and white photo of a female boxer in a guard stance">
      <defs>
        <linearGradient id="boxer" x1="0" y1="0" x2="1" y2="1">
          <stop offset="0" stop-color="#5a5a5a"/>
          <stop offset=".6" stop-color="#2a2a2a"/>
          <stop offset="1" stop-color="#111"/>
        </linearGradient>
      </defs>
      <path d="M360 290 C 230 320, 120 400, 110 520 C 104 600, 150 660, 210 690 L360 690 Z" fill="url(#boxer)"/>
    </svg>
    <svg class="layer" viewBox="0 0 360 764" aria-hidden="true">
      <path d="M300 0 L360 0 L360 40 C 330 120, 330 200, 360 250 L360 262 C 318 206, 310 120, 300 0 Z" fill="var(--yellow)"/>
      <path d="M360 270 C 220 300, 100 390, 92 520 C 86 610, 140 676, 200 700 L218 700 C 160 672, 112 606, 118 522 C 126 404, 236 320, 360 296 Z" fill="var(--yellow)"/>
      <path d="M0 680 L360 676 L360 746 L0 750 Z" fill="var(--yellow)"/>
    </svg>
    <span class="brand cover__brand"><span class="brand__mark"></span>RIDGE PUNCH</span>
    <h1 class="cover__title head">Get fit lose weight<br>&amp; feel great</h1>
    <p class="cover__url">www.ridgepunch.com.au</p>
  </article>
</section>

<!-- Inside of the trifold -->
<section class="sheet sheet--inside" aria-label="Brochure inside">

  <article class="panel panel--light">
    <svg class="layer" viewBox="0 0 360 764" role="img" aria-label="Faded photo of boxing gloves during a training session">
      <defs>
        <linearGradient id="gloves" x1="0" y1="0" x2="1" y2="1">
          <stop offset="0" stop-color="#e6e6e6"/>
          <stop offset="1" stop-color="#b8b8b8"/>
        </linearGradient>
      </defs>
      <path d="M150 300 C 240 290, 330 330, 360 380 L360 764 L150 764 Z" fill="url(#gloves)" opacity=".6"/>
    </svg>
    <p class="tag">Tailored programs</p>
    <div class="benefit" style="top:112px">
      <p class="benefit__text">Our programs are structured so that members of all fitness levels feel confident &amp; comfortable during their start-up phase allowing you to quickly build your fitness</p>
    </div>
    <div class="benefit" style="top:258px">
      <h2 class="benefit__title">Injury prevention</h2>
      <p class="benefit__text">Our training systems include techniques that will help you avoid injuries and build balanced strength</p>
    </div>
    <div class="benefit" style="top:396px">
      <h2 class="benefit__title">Strengthen &amp; tone your core</h2>
      <p class="benefit__text">You're core muscles are some of you're most important muscles. Each workout you do incorporates core exercises to help avoid injuries and make you're total body stronger</p>
    </div>
    <p class="inside-url">www.ridgepunch.com.au</p>
  </article>

  <article class="panel panel--energy">
    <svg class="layer" viewBox="0 0 360 764" role="img" aria-label="Photo of a boxer's gloved hands mid punch">
      <defs>
        <linearGradient id="punch" x1="0" y1="0" x2="1" y2="1">
          <stop offset="0" stop-color="#8a8a8a"/>
          <stop offset="1" stop-color="#dcdcdc"/>
        </linearGradient>
      </defs>
      <path d="M0 330 C 120 300, 260 300, 360 260 L360 764 L0 764 Z" fill="url(#punch)"/>
      <path d="M0 680 L360 680 L360 764 L0 764 Z" fill="#ececec"/>
    </svg>
    <svg class="layer" viewBox="0 0 360 764" aria-hidden="true">
      <path d="M0 0 L40 0 C 20 120, 10 220, 0 300 Z" fill="var(--yellow)"/>
      <path d="M0 312 C 120 282, 260 282, 360 242 L360 262 C 260 302, 120 302, 0 332 Z" fill="var(--yellow)"/>
    </svg>
    <div class="benefit benefit--yellow" style="left:56px;top:64px;width:270px">
      <h2 class="benefit__title">Wake up with more energy</h2>
      <p class="benefit__text">Every class you'll do will have you filled with energy the will pump you up for the rest of your day</p>
    </div>
  </article>

  <article class="panel panel--support">
    <svg class="layer" viewBox="0 0 360 764" role="img" aria-label="Photo of a woman stretching on the grass outdoors">
      <defs>
        <linearGradient id="grass" x1="0" y1="0" x2="1" y2="1">
          <stop offset="0" stop-color="#6f8a3e"/>
          <stop offset="1" stop-color="#2f4220"/>
        </linearGradient>
      </defs>
      <path d="M360 480 C 270 510, 200 580, 180 680 L180 764 L360 764 Z" fill="url(#grass)"/>
    </svg>
    <svg class="layer" viewBox="0 0 360 764" aria-hidden="true">
      <path d="M360 462 C 262 494, 186 568, 164 676 L164 764 L180 764 L180 680 C 200 582, 272 512, 360 482 Z" fill="var(--yellow)"/>
    </svg>
    <div class="benefit" style="left:36px;top:64px">
      <h2 class="benefit__title">Sleep better</h2>
      <p class="benefit__text">One of the best parts of exercise is the benefit it has on your sleeping patterns. You'll sleep deeper &amp; more sound</p>
    </div>
    <div class="benefit" style="left:36px;top:212px">
      <h2 class="benefit__title">Supportive environment</h2>
      <p class="benefit__text">At RIDGE PUNCH you'll be surrounded by trainers &amp; other members who are there to encourage &amp; motivate you to reach your goals and to get you moving more.</p>
    </div>
  </article>

  <p class="promise">COMPLETE AFFORDABILITY &amp; NO JUDGEMENTS GUARANTEED!</p>
</section>

</body>
</html>
```